Beautiful Simple and Clean WEbsite for Life Coach

Looking for a simple clean site website for life coach for educators. A home page will have an embedded opt-in form, menu bar will be
Work With Me - page for my coaching program and link to online calendar for booking
PRAISE - testimonials
ABOUT
PODCAST
I can supply images and a site I would like it modeled after is https://nadiafenrow.com/
My current website at www.tessaquorm.com is too dark. I am looking for the white space, pink and magenta. Feel free to use images from the site

Industry/Entity Type

Life Coaching

Number of Pages Required

4 page

Font styles to use
Serif

Colors
E54698
E96AAD
F1A4CE
F9D9EA
FCEFF6

Requirements
Must have
• See attached files for must-haves, Lots of white space, opt-in from for freebie is the most prominent on home page
Nice to have
• refer to Nadia Fenrow websites
Should not have
• dark colors, any balck background

```html
<!DOCTYPE html>
<html lang="en">
<head>
<meta charset="utf-8">
<title>Tessa Quorm — Life Coach for Educators</title>
<link rel="stylesheet" href="https://fonts.googleapis.com/css2?family=Playfair+Display:wght@400&family=Work+Sans:wght@400;500;600&display=swap">
<style>
:root{
  --pink:#f9a8b4;
  --pink-pale:#fde1e5;
  --pink-band:#fcc5ce;
  --blush:#fdf1ec;
  --rose-mist:#fbe9ed;
  --mauve:#a07e89;
  --mauve-dark:#8f6f7a;
  --ink:#3d3739;
  --ink-soft:#6a6266;
  --white:#ffffff;
  --line:#d9c5cb;
}
*{box-sizing:border-box;margin:0;padding:0}
html,body{width:1200px;height:4155px;overflow:hidden;background:var(--white)}
body{position:relative;font-family:"Work Sans",sans-serif;color:var(--ink)}
.abs{position:absolute}
.serif{font-family:"Playfair Display",serif;font-weight:400}
.photo{position:absolute}
.btn-outline{position:absolute;border:2px solid var(--mauve);color:var(--mauve);font-size:13px;font-weight:600;letter-spacing:.06em;display:flex;align-items:center;justify-content:center;gap:8px;text-transform:uppercase}
.btn-outline svg{width:18px;height:10px}
.rule{position:absolute;height:3px;background:var(--mauve)}
.dots{position:absolute;background-image:radial-gradient(circle,#d7c3c8 1.4px,transparent 1.6px);background-size:13px 13px}
.center{text-align:center}

/* header */
.logo{left:100px;top:18px;font-size:40px;color:#ef8ea1}
.nav{top:34px;font-size:14px;color:var(--ink-soft);letter-spacing:.03em}
.nav-active{border-bottom:3px solid #f2b6c0;padding-bottom:10px}
.book-online{left:942px;top:24px;width:171px;height:41px;background:#dfe4e0;color:var(--ink-soft);font-size:14px;display:flex;align-items:center;justify-content:center;letter-spacing:.03em}

/* hero */
.hero-shadow{left:98px;top:240px;width:460px;height:315px;background:var(--pink-pale)}
.hero-card{left:115px;top:215px;width:458px;height:325px;background:var(--pink);color:var(--white)}
.hero-title{position:absolute;left:0;right:0;top:58px;font-size:41px;line-height:40px;letter-spacing:.02em}
.hero-sub{position:absolute;left:0;right:0;top:150px;font-size:15px;line-height:26px;letter-spacing:.03em;color:#fff3f5}
.hero-btn{left:104px;top:230px;width:218px;height:42px;border:2px solid var(--white);color:var(--white);font-size:11px;font-weight:500}

/* sections */
.h2{font-size:38px;color:var(--ink)}
.body-text{font-size:15px;line-height:24.6px;color:var(--ink)}
.card-podcast{position:absolute;top:2910px;width:313px;height:289px;background:var(--white);border-radius:0 60px 0 60px;text-align:center}
.pod-icon{position:absolute;left:130px;top:43px;width:52px;height:52px;border-radius:50%;background:#f39aa8;border:4px solid #fcd0d7}
.pod-title{position:absolute;left:0;right:0;top:104px;font-size:15px;font-weight:600;line-height:23px;letter-spacing:.04em;color:var(--ink)}
.pod-desc{position:absolute;left:0;right:0;top:157px;font-size:12px;line-height:18px;color:var(--ink-soft)}
.pod-btn{left:90px;top:208px;width:138px;height:35px;font-size:11px}

.field{position:absolute;left:626px;width:427px;border:2px solid var(--line);display:flex;align-items:center;gap:10px;padding-left:18px;font-size:12px;color:var(--ink-soft)}
.field svg{width:13px;height:13px;stroke:#b8a4aa;fill:none;stroke-width:1.6}

/* footer */
.footer{left:0;top:3944px;width:1200px;height:211px;background:var(--mauve)}
.foot-link{position:absolute;top:4002px;font-size:13px;font-weight:600;color:var(--white);letter-spacing:.04em;transform:translateX(-50%)}
.social{position:absolute;top:4086px;width:32px;height:32px;border-radius:50%;background:var(--white)}
</style>
</head>
<body>

<!-- header -->
<div class="abs serif logo">Tessa Quorm</div>
<nav>
  <div class="abs nav nav-active" style="left:429px">WORK WITH ME</div>
  <div class="abs nav" style="left:602px">PRAISE</div>
  <div class="abs nav" style="left:716px">ABOUT</div>
  <div class="abs nav" style="left:827px">PODCAST</div>
  <div class="abs book-online">BOOK ONLINE</div>
</nav>

<!-- hero -->
<div class="photo" role="img" aria-label="Portrait of the coach in a straw sun hat and denim jacket in a field" style="left:344px;top:116px;width:769px;height:534px;background:linear-gradient(180deg,#8c8f78 0%,#b6a896 45%,#9a8a86 100%)"></div>
<div class="abs hero-shadow"></div>
<section class="abs hero-card center">
  <h1 class="serif hero-title">LIFE COACH FOR<br>EDUCATORS</h1>
  <p class="hero-sub">Being Overworked, Being Overwhelmed<br>and not having Work - Life Balance</p>
  <a class="btn-outline hero-btn">BOOK AN APPOINTMENT <svg viewBox="0 0 18 10"><path d="M0 5h16M12 1l4 4-4 4" stroke="#fff" fill="none" stroke-width="1.3"/></svg></a>
</section>

<!-- opt-in -->
<section>
  <h2 class="abs serif h2 center" style="left:0;width:1200px;top:750px;line-height:45px">Why School Leaders Need<br>Balance to Succeed</h2>
  <p class="abs center" style="left:0;width:1200px;top:866px;font-size:17px;line-height:29px">DISCOVER the secrets on how to prioritize the items on an overwhelming<br>to-do list to get the job done successfully.</p>
  <a class="btn-outline" style="left:471px;top:950px;width:248px;height:52px">DOWNLOAD FREE GUIDE <svg viewBox="0 0 18 10"><path d="M0 5h16M12 1l4 4-4 4" stroke="#a07e89" fill="none" stroke-width="1.3"/></svg></a>
</section>

<!-- about -->
<section class="abs" style="left:0;top:1056px;width:1200px;height:667px;background:var(--blush)"></section>
<div class="dots" style="left:84px;top:1157px;width:122px;height:121px"></div>
<div class="dots" style="left:1011px;top:1561px;width:123px;height:122px"></div>
<div class="abs" style="left:290px;top:1135px;width:828px;height:528px;background:var(--white)"></div>
<div class="abs" style="left:123px;top:1187px;width:392px;height:424px;background:var(--white);border:1px solid #d8cccf"></div>
<div class="photo" role="img" aria-label="The coach in a sun hat reading a book outdoors" style="left:131px;top:1195px;width:374px;height:407px;background:linear-gradient(180deg,#b7a27a 0%,#d9cdb4 60%,#e9e6e3 100%)"></div>
<h2 class="abs serif h2" style="left:589px;top:1222px">ABOUT ME</h2>
<div class="rule" style="left:589px;top:1272px;width:50px"></div>
<div class="abs body-text" style="left:587px;top:1296px;width:480px">
  <p>I’m a Life Coach. &nbsp;I am also a retired Elementary School Principal who loves other educators and everything in education. In my coaching practice, I empower my clients with simple survival skills to succeed at their school and in their life. They have more time, less stress, and yell less.</p>
  <p style="margin-top:5px">If you would like to learn more about how to manage stress and overwhelm, and how to feel better no matter what the circumstances I am your gal.</p>
</div>
<div class="photo" role="img" aria-label="Handwritten signature of the coach" style="left:597px;top:1518px;width:250px;height:70px;background:linear-gradient(90deg,#fce3e8,#fbeef1)"></div>

<!-- work with me -->
<section class="abs" style="left:0;top:1724px;width:661px;height:555px;background:var(--pink-band)"></section>
<h2 class="abs serif h2 center" style="left:0;width:622px;top:1867px;color:#4a3f43">WORK WITH ME</h2>
<div class="rule" style="left:286px;top:1915px;width:50px"></div>
<p class="abs body-text center" style="left:124px;top:1940px;width:374px;line-height:23.8px">I’m a Life Coach. &nbsp;I am also a retired Elementary School Principal who loves other educators and everything in education. In my coaching practice, I empower my clients with simple survival skills to succeed at their</p>
<a class="btn-outline" style="left:211px;top:2086px;width:174px;height:46px;font-size:13px;color:#a07e89">LEARN MORE <svg viewBox="0 0 18 10"><path d="M0 5h16M12 1l4 4-4 4" stroke="#e6a9b3" fill="none" stroke-width="1.3"/></svg></a>
<div class="dots" style="left:958px;top:2102px;width:126px;height:124px"></div>
<div class="abs" style="left:535px;top:1811px;width:522px;height:384px;background:var(--white);border:1px solid #d8cccf"></div>
<div class="photo" role="img" aria-label="The coach in a teal outfit reading a book on a red-cushioned wicker sofa" style="left:550px;top:1826px;width:495px;height:356px;background:linear-gradient(135deg,#7d6e62 0%,#b8343c 45%,#3fc7b0 75%,#8a7d72 100%)"></div>

<!-- praise -->
<section>
  <h2 class="abs serif h2 center" style="left:0;width:1175px;top:2360px">PRAISE</h2>
  <div class="rule" style="left:562px;top:2413px;width:50px"></div>
  <svg class="abs" style="left:578px;top:2464px" width="50" height="40" viewBox="0 0 50 40"><path d="M6 4a10 10 0 1 1 6 18c0 6-3 10-9 14 10-2 17-10 17-20A10 10 0 0 0 6 4zM30 4a10 10 0 1 1 6 18c0 6-3 10-9 14 10-2 17-10 17-20A10 10 0 0 0 30 4z" fill="#e3d6da"/></svg>
  <p class="abs center" style="left:290px;width:620px;top:2515px;font-size:16px;line-height:25px;color:var(--ink-soft)">Lorem ipsum dolor sit amet, consectetur adipiscing elit, sed do eiusmod tempor incididunt ut labore et dolore magna aliqua. Ut enim ad minim veniam, quis nostrud exercitation ullamco laboris nisi</p>
  <svg class="abs" style="left:152px;top:2545px" width="42" height="24" viewBox="0 0 42 24"><path d="M41 12H2M12 2L2 12l10 10" stroke="#a07e89" fill="none" stroke-width="2.2"/></svg>
  <svg class="abs" style="left:1002px;top:2545px" width="42" height="24" viewBox="0 0 42 24"><path d="M1 12h39M30 2l10 10-10 10" stroke="#a07e89" fill="none" stroke-width="2.2"/></svg>
  <p class="abs center" style="left:0;width:1208px;top:2610px;font-size:16px;font-weight:600;color:#4a4346">Maren Tolliver</p>
  <p class="abs center" style="left:0;width:1208px;top:2636px;font-size:14px;color:var(--ink-soft)">Weight Coach for Military Moms</p>
</section>

<!-- podcasts -->
<section class="abs" style="left:0;top:2742px;width:1200px;height:537px;background:var(--rose-mist)"></section>
<h2 class="abs serif h2 center" style="left:0;width:1200px;top:2798px">PODCATS</h2>
<div class="rule" style="left:585px;top:2851px;width:58px"></div>

<div class="card-podcast" style="left:127px">
  <div class="pod-icon"></div>
  <h3 class="pod-title">MOTHER’S DAY CAN BE FILLED<br>WITH CONFLICTING</h3>
  <p class="pod-desc">It’s Mother’s Day weekend, and I am<br>traveling to Texas to see my Mom</p>
  <a class="btn-outline pod-btn">LISTEN NOW <svg viewBox="0 0 18 10"><path d="M0 5h16M12 1l4 4-4 4" stroke="#a07e89" fill="none" stroke-width="1.3"/></svg></a>
</div>
<div class="card-podcast" style="left:463px">
  <div class="pod-icon"></div>
  <h3 class="pod-title">MOTHER’S DAY CAN BE FILLED<br>WITH CONFLICTING</h3>
  <p class="pod-desc">It’s Mother’s Day weekend, and I am<br>traveling to Texas to see my Mom</p>
  <a class="btn-outline pod-btn">LISTEN NOW <svg viewBox="0 0 18 10"><path d="M0 5h16M12 1l4 4-4 4" stroke="#a07e89" fill="none" stroke-width="1.3"/></svg></a>
</div>
<div class="card-podcast" style="left:800px">
  <div class="pod-icon"></div>
  <h3 class="pod-title">MOTHER’S DAY CAN BE FILLED<br>WITH CONFLICTING</h3>
  <p class="pod-desc">It’s Mother’s Day weekend, and I am<br>traveling to Texas to see my Mom</p>
  <a class="btn-outline pod-btn">LISTEN NOW <svg viewBox="0 0 18 10"><path d="M0 5h16M12 1l4 4-4 4" stroke="#a07e89" fill="none" stroke-width="1.3"/></svg></a>
</div>

<!-- book appointment -->
<div class="abs" style="left:105px;top:3374px;width:458px;height:428px;background:#f3a6b4;border-radius:0 60px 0 60px"></div>
<div class="photo" role="img" aria-label="The coach seated on a sofa with a laptop beside a lamp" style="left:124px;top:3390px;width:439px;height:412px;border-radius:0 60px 0 60px;background:linear-gradient(135deg,#6b5a4a 0%,#c8a15a 40%,#8d7a70 70%,#4e4a4d 100%)"></div>
<h2 class="abs serif h2" style="left:621px;top:3385px;font-size:34px">BOOK APPOINTMENT</h2>
<div class="rule" style="left:624px;top:3436px;width:56px"></div>
<div class="field" style="top:3468px;height:44px"><svg viewBox="0 0 14 14"><rect x="3" y="6" width="8" height="7"/><path d="M4.5 6V4a2.5 2.5 0 0 1 5 0v2"/></svg>Name</div>
<div class="field" style="top:3526px;height:43px"><svg viewBox="0 0 14 14"><path d="M3 1l2.5 3-1.5 1.5a8 8 0 0 0 4.5 4.5L10 8.5 13 11l-1.5 2C6 13 1 8 1 2.5z"/></svg>Phone</div>
<div class="field" style="top:3578px;height:43px"><svg viewBox="0 0 14 14"><rect x="1" y="3" width="12" height="9"/><path d="M1 3l6 5 6-5"/></svg>Email address</div>
<div class="field" style="top:3636px;height:90px;align-items:flex-start;padding-top:16px">Leave a message</div>
<a class="abs" style="left:626px;top:3742px;width:216px;height:44px;background:#f6a5b2;color:var(--white);font-size:11px;font-weight:500;letter-spacing:.06em;display:flex;align-items:center;justify-content:center;gap:10px">SEND YOUR MESSAGE <svg width="18" height="10" viewBox="0 0 18 10"><path d="M0 5h16M12 1l4 4-4 4" stroke="#fff" fill="none" stroke-width="1.3"/></svg></a>

<!-- footer -->
<footer class="abs footer"></footer>
<div class="abs" style="left:564px;top:3889px;width:84px;height:84px;border-radius:50%;border:2px solid #e7dadd;background:var(--white)"></div>
<div class="abs" style="left:571px;top:3896px;width:70px;height:70px;border-radius:50%;background:var(--mauve)"></div>
<svg class="abs" style="left:596px;top:3914px" width="20" height="26" viewBox="0 0 20 26"><path d="M10 25V2M2 10l8-8 8 8" stroke="#fff" fill="none" stroke-width="1.8"/></svg>
<a class="foot-link" style="left:232px">HOME</a>
<a class="foot-link" style="left:389px">WORK WITH ME</a>
<a class="foot-link" style="left:552px">PRAISE</a>
<a class="foot-link" style="left:686px">ABOUT</a>
<a class="foot-link" style="left:823px">PODCAST</a>
<a class="foot-link" style="left:987px">BOOK ONLINE</a>
<p class="abs center" style="left:0;width:1200px;top:4044px;font-size:12px;color:var(--white)">Copyright © 2022 <span style="text-decoration:underline">Tessa Quorm</span>. All Right Reserved</p>
<div class="social" style="left:521px" aria-label="Social profile"></div>
<div class="social" style="left:561px" aria-label="Social profile"></div>
<div class="social" style="left:603px" aria-label="Social profile"></div>
<div class="social" style="left:645px" aria-label="Social profile"></div>

</body>
</html>
```